VEHICLE WRAP

2022 VORLAND TEK CARGOLINE XL MUST HAVE UNIFIED LOOK OPEN TO DIFFERENT LOOKS BUT MUST BE UNIFIES TO THE OTHER TRCUKS WE HAVE IN THE BUSINESS PLEASE SEE PHOTOS BUT SERVICES SAME AS BRISKEN LOCKSMITH TRUCK

Industry/Entity Type

LOCKSMITH

Font styles to use
Serif
Sans Serif

Colors
EB3D1F
EC4F4E
F09395
F8D3D4
FCEDEE

Requirements
Must have
• SAME COLORS DARK GREY RED
Should not have
• NO NEW COLORS

```html
<!DOCTYPE html>
<html lang="en">
<head>
<meta charset="utf-8">
<title>Brisken Locksmith – Rear Door Wrap</title>
<link rel="stylesheet" href="https://fonts.googleapis.com/css2?family=Michroma&family=Roboto:ital,wght@0,700;1,700&display=swap">
<style>
  :root {
    --backdrop: #ececec;
    --wrap-red: #e2524f;
    --wrap-grey: #434345;
    --band-white: #fcedee;
    --text-white: #ffffff;
    --text-red: #eb3d1f;
    --divider: #f8d3d4;
  }
  * { box-sizing: border-box; margin: 0; padding: 0; }
  html, body {
    width: 1200px; height: 800px; overflow: hidden;
    background: var(--backdrop);
  }
  .canvas { position: relative; width: 1200px; height: 800px; }

  .wrap {
    position: absolute; left: 380px; top: 110px;
    width: 440px; height: 520px;
    display: flex; border-radius: 36px 36px 6px 6px; overflow: hidden;
  }
  .door { position: relative; height: 100%; width: 50%; }
  .door--left { background: var(--wrap-red); }
  .door--right { background: var(--wrap-grey); border-left: 3px solid var(--divider); }

  .brand {
    position: absolute; left: 30px; top: 80px; width: 160px;
    display: flex; flex-direction: column; align-items: center; gap: 18px;
  }
  .brand__dot {
    width: 84px; height: 84px; border-radius: 50%;
    background: var(--text-white);
  }
  .brand__name {
    font-family: "Roboto", sans-serif; font-weight: 700;
    color: var(--text-white); font-size: 20px; letter-spacing: 1px;
    text-align: center; line-height: 1.2;
  }

  .contact {
    position: absolute; left: 0; right: 0; top: 390px; text-align: center;
    font-family: "Roboto", sans-serif; font-weight: 700; color: var(--text-white);
    font-size: 15px; letter-spacing: 0.5px; line-height: 1.4;
  }
  .contact__hours { font-style: italic; }

  .service-bands { position: absolute; left: 0; right: 0; top: 96px; }
  .service-band {
    height: 19px; margin-bottom: 23px; background: var(--band-white);
    font-family: "Michroma", sans-serif; font-size: 8px; color: var(--text-red);
    line-height: 19px; white-space: nowrap; overflow: hidden; padding-left: 4px;
  }
  .service-band--inset { padding-left: 28px; }

  .segments {
    position: absolute; left: 52px; top: 290px; list-style: none;
    font-family: "Michroma", sans-serif; color: var(--text-white); font-size: 12px;
  }
  .segments li { position: relative; padding-left: 16px; margin-bottom: 30px; }
  .segments li::before {
    content: ""; position: absolute; left: 0; top: 2px;
    width: 5px; height: 5px; border-radius: 50%; background: var(--text-white);
  }

  .web {
    position: absolute; left: 0; right: 0; top: 462px; text-align: center;
    font-family: "Michroma", sans-serif; color: var(--text-white); font-size: 12px;
  }
</style>
</head>
<body>
<main class="canvas">
  <section class="wrap" aria-label="Rear door wrap">
    <div class="door door--left">
      <div class="brand">
        <span class="brand__dot"></span>
        <p class="brand__name">BRISKEN<br>LOCKSMITH</p>
      </div>
      <div class="contact">
        <p class="contact__address">2280 ALDER CREST RD</p>
        <p class="contact__hours">24/7 EMERGENCY</p>
      </div>
    </div>
    <div class="door door--right">
      <div class="service-bands">
        <p class="service-band">KEYLESS ENTRY LOCKS . SAFES . HARDWARE</p>
        <p class="service-band">HIGH SECURITY LOCKS . HANDICAP OPERATORS</p>
        <p class="service-band service-band--inset">ACCESS CONTROL . ALARM SYSTEMS</p>
        <p class="service-band">CAR KEYS . REMOTES . PROGRAMMING</p>
      </div>
      <ul class="segments">
        <li>Residential</li>
        <li>Commercial</li>
        <li>Automotive</li>
      </ul>
      <p class="web">www.briskenlock.com</p>
    </div>
  </section>
</main>
</body>
</html>
```